Business card design for a teacher - double sided, sleek design.

My name is Dalia and I am an online Arabic language teacher. I am looking for a beautiful business card design for my online teaching business.

The cards will be printed in 85mm x 55mm size.
The card can be either portrait or landscape.

The design should contain my logo on one side and information on the other.

The design needs to be clean and modern. Use of subtle Arabic geometric patterns would be nice. Icons for the social media information on the card should also match the design theme.

My logo font is Consolas, which is a Monospace font.

Business card design should be delivered with editable PSD or EPS files in the handover.

Thanks

Dalia

----

Information on the back:

URL: www.lughapathway.net [this should stand out more than other details]
Email: info@lughapathway.net
Instagram: @lughapathway
Facebook: facebook.com/lughapathway
Skype: lughapathway

My brand colours are shown in the logo attached. These are:
- Teal green - 4DC9C1
- Mango yellow - FFD600

Target Market(s)

- Young professionals
- Expatriates
- Women and Men

Industry/Entity Type

Education

Contact Information for Business Card

Information on the back:

Skype: lughapathway

- Teal green - 4DC9C1
- Mango yellow - FFD600

Font styles to use
Other font styles liked:
• Any font complimentary to my logo font which is a Monospace font called Consolas.

Colors

Designer to choose colors to be used in the design.

Requirements
Must have
• - Aesthetically pleasing look
• - Complimentary design with existing logo
Nice to have
• Arabic geometrical patterns

```html
<!DOCTYPE html>
<html lang="en">
<head>
<meta charset="utf-8">
<title>Lugha Pathway – Business Card</title>
<link rel="stylesheet" href="https://fonts.googleapis.com/css2?family=Inconsolata:wght@700&family=Open+Sans:wght@400&family=Montserrat:wght@600&display=swap">
<style>
  :root {
    --teal: #4dc9c1;
    --mango: #ffd600;
    --ink: #5a5a5a;
    --dark: #333;
    --paper: #ffffff;
    --pattern-tone: #f1f3f3;
    --stage: #2a2a2a;
  }
  * { box-sizing: border-box; margin: 0; padding: 0; }
  html, body { width: 1200px; height: 900px; overflow: hidden; }
  body {
    background: var(--stage);
    display: flex;
    align-items: center;
    justify-content: center;
    gap: 40px;
  }
  .card {
    position: relative;
    width: 540px;
    height: 350px;
    border-radius: 26px;
    overflow: hidden;
    background: var(--paper);
  }
  .card__pattern {
    position: absolute;
    inset: 0;
    background: linear-gradient(135deg, var(--paper) 0%, var(--pattern-tone) 50%, var(--paper) 100%);
  }
  .card__rule {
    position: absolute;
    left: 0; right: 0;
    top: 262px;
    height: 2px;
  }
  .card__label {
    position: absolute;
    top: 245px;
    padding: 0 18px;
    height: 36px;
    display: flex;
    align-items: center;
    background: var(--paper);
    border: 2px solid;
    white-space: nowrap;
  }

  /* Front */
  .front .card__rule { background: var(--teal); }
  .front .card__label {
    left: 170px;
    border-color: var(--teal);
    font-family: "Montserrat", sans-serif;
    font-weight: 600;
    font-size: 14px;
    letter-spacing: 3px;
    color: var(--ink);
  }
  .brand {
    position: absolute;
    left: 0;
    right: 0;
    top: 95px;
    display: flex;
    align-items: center;
    justify-content: center;
    gap: 18px;
  }
  .brand__dot {
    width: 26px;
    height: 26px;
    border-radius: 50%;
    background: var(--teal);
  }
  .brand__name {
    font-family: "Inconsolata", monospace;
    font-weight: 700;
    font-size: 46px;
    letter-spacing: 5px;
    color: var(--teal);
    text-transform: uppercase;
    white-space: nowrap;
  }

  /* Back */
  .back .card__rule { background: var(--mango); }
  .back .card__label {
    right: 50px;
    border-color: var(--mango);
    font-family: "Inconsolata", monospace;
    font-weight: 700;
    font-size: 18px;
    letter-spacing: 3px;
    color: var(--teal);
  }
  .contacts {
    position: absolute;
    left: 150px;
    top: 78px;
    list-style: none;
    font-family: "Open Sans", sans-serif;
    font-size: 15px;
    color: var(--dark);
  }
  .contacts li {
    display: flex;
    align-items: center;
    gap: 12px;
    height: 32px;
  }
  .contacts__icon {
    width: 22px;
    height: 22px;
    background: var(--teal);
    display: flex;
    align-items: center;
    justify-content: center;
    flex: none;
  }
</style>
</head>
<body>

  <section class="card front" aria-label="Card front">
    <div class="card__pattern" role="img" aria-label="Subtle Arabic geometric lattice pattern"></div>
    <div class="brand">
      <span class="brand__dot"></span>
      <span class="brand__name">Lugha Pathway</span>
    </div>
    <div class="card__rule"></div>
    <div class="card__label">ARABIC LANGUAGE TEACHER</div>
  </section>

  <section class="card back" aria-label="Card back">
    <div class="card__pattern" role="img" aria-label="Subtle Arabic geometric lattice pattern"></div>
    <ul class="contacts">
      <li><span class="contacts__icon"></span>/lughapathway</li>
      <li><span class="contacts__icon"></span>/lughapathway</li>
      <li><span class="contacts__icon"></span>lughapathway</li>
      <li>
        <span class="contacts__icon">
          <svg width="14" height="10" viewBox="0 0 14 10" aria-hidden="true">
            <rect x="0.75" y="0.75" width="12.5" height="8.5" fill="none" stroke="#fff" stroke-width="1.5"/>
            <polyline points="1,1 7,6 13,1" fill="none" stroke="#fff" stroke-width="1.5"/>
          </svg>
        </span>info@lughapathway.net
      </li>
    </ul>
    <div class="card__rule"></div>
    <div class="card__label">www.lughapathway.net</div>
  </section>

</body>
</html>
```